PPT Template Graphic Design for Firm Serving Sales & Mrkting Executives in High-Tech Comopanies

Brookvane seeks a graphic design for a PowerPoint template for corporate presentations.
We are a workforce solutions company that specializes in finding and managing contractors for sales and marketing organizations in high-tech companies. We can also manage entire processes with our 'managed services' solution, for existing clients. We are unique in our exclusive focus on sales & marketing, our consultative approach that works with clients to leverage contractors, not just to fill immediate resource gaps they may have, but also to achieve immediate and longer term business goals of their organization. We offer the dual advantage of flexibility as clients may find within a boutique firm, and the scalability of a global company which means that regardless of whether clients need one contractor or several, locally or in foreign markets, we can help.
We will use this PPT template to present what we do to help clients, and how we are different from the competition to prospective clients. We might also use this PPT template to present proposals.

Reason: We would love to see some more design options! Also, we have guaranteed the project since we first posted. Thank you!

Target Market(s)

Executives in sales and marketing organizations of high tech companies, including VP of Sales, VP marketing, CEO, CFO and heads of HR departments.

Industry/Entity Type

Graphic Design

Requirements
Must have
• Template must be simple, elegant, classy. Please include a cover page, supporting pages (for content of presentation) and concluding ("Thank You") page. Design must include our logo & tagline (see attached), and provide recommendations for heading font, copy font and ‘bullet’ styles. Please locate company name on bottom right of template. Design should be in the same family of the look and feel of our website (www.brookvane-example.com). We would like the design to convey simplicity and elegance. We’d also like it to reflect the personality of our firm: friendly and approachable, with a high level of professionalism. Design should feel confident, and up-to-date in its look. Template must be both MAC and PC compatible.
Nice to have
• Same template developed for PPT, imported into a Prezi format as well. We need the PPT template for sure, but one in Prezi would be great to have as well - to enable more professional looking format for presentations.

```html
<!DOCTYPE html>
<html lang="en">
<head>
<meta charset="utf-8">
<title>Brookvane – Content Slide</title>
<link rel="stylesheet" href="https://fonts.googleapis.com/css2?family=Oswald:wght@600&family=Arimo:wght@400;700&display=swap">
<style>
  :root {
    --page-bg: #eef0f2;
    --band-white: #ffffff;
    --title-orange: #f26a21;
    --subtitle-grey: #6b6b6b;
    --heading-purple: #5a1670;
    --bullet-blue: #1a9ad6;
    --bullet-mark: #1e1e1e;
    --art-blue: #2a9fd6;
    --art-orange: #f47a2a;
  }
  html, body {
    margin: 0;
    padding: 0;
    width: 1200px;
    height: 900px;
    overflow: hidden;
  }
  body {
    position: relative;
    background: var(--page-bg);
    font-family: "Arimo", Arial, sans-serif;
  }
  .title-band {
    position: absolute;
    left: 0; top: 50px;
    width: 1200px; height: 78px;
    background: var(--band-white);
    text-align: center;
  }
  .project-title {
    margin: 6px 0 0;
    font-family: "Oswald", "Arial Narrow", sans-serif;
    font-weight: 600;
    font-size: 33px;
    line-height: 40px;
    color: var(--title-orange);
    letter-spacing: 0.5px;
  }
  .project-subtitle {
    margin: 0;
    font-size: 20px;
    line-height: 24px;
    color: var(--subtitle-grey);
  }
  .content-panel {
    position: absolute;
    left: 57px; top: 192px;
    width: 1107px; height: 480px;
    background: var(--band-white);
  }
  .section-heading {
    position: absolute;
    left: 25px; top: 30px;
    width: 1008px;
    margin: 0;
    padding-bottom: 10px;
    border-bottom: 2px solid var(--heading-purple);
    display: flex;
    align-items: center;
    gap: 14px;
    font-size: 30px;
    font-weight: 400;
    color: var(--heading-purple);
  }
  .section-heading svg { flex: none; }
  .bullet-list {
    position: absolute;
    left: 78px; top: 112px;
    margin: 0; padding: 0;
    list-style: none;
  }
  .bullet-list li {
    display: flex;
    align-items: center;
    height: 56px;
    font-size: 27px;
    color: var(--bullet-blue);
  }
  .bullet-list li svg { margin-right: 26px; flex: none; }
  .teamwork-art {
    position: absolute;
    left: 663px; top: 128px;
    width: 398px; height: 285px;
    border-radius: 6px;
    background: linear-gradient(90deg, var(--art-blue) 0%, #8fc8e6 45%, #f7b68a 60%, var(--art-orange) 100%);
    opacity: 0.85;
  }
  .footer-band {
    position: absolute;
    left: 0; top: 775px;
    width: 1200px; height: 90px;
    background: var(--band-white);
  }
  .brand-name {
    position: absolute;
    right: 40px; top: 22px;
    margin: 0;
    font-size: 40px;
    font-weight: 700;
    line-height: 46px;
    color: var(--title-orange);
  }
</style>
</head>
<body>
  <header class="title-band">
    <h1 class="project-title">PROJECT TITLE HERE</h1>
    <p class="project-subtitle">Sub title here</p>
  </header>

  <main class="content-panel">
    <h2 class="section-heading">
      <svg width="30" height="28" viewBox="0 0 30 28" aria-hidden="true">
        <path d="M2 15 L11 25 L28 3" fill="none" stroke="var(--heading-purple)" stroke-width="5" stroke-linejoin="round"/>
      </svg>
      Lorem ipsum dlolor sit ipsum ipsum
    </h2>
    <ul class="bullet-list">
      <li><svg width="11" height="16" viewBox="0 0 11 16" aria-hidden="true"><path d="M2 2 L8 8 L2 14" fill="none" stroke="var(--bullet-mark)" stroke-width="3.5"/></svg>Lorem ipsum dlolor sit ipsum ipsum</li>
      <li><svg width="11" height="16" viewBox="0 0 11 16" aria-hidden="true"><path d="M2 2 L8 8 L2 14" fill="none" stroke="var(--bullet-mark)" stroke-width="3.5"/></svg>Lorem ipsum dlolor sit ipsum ipsum</li>
      <li><svg width="11" height="16" viewBox="0 0 11 16" aria-hidden="true"><path d="M2 2 L8 8 L2 14" fill="none" stroke="var(--bullet-mark)" stroke-width="3.5"/></svg>Lorem ipsum dlolor sit ipsum ipsum</li>
      <li><svg width="11" height="16" viewBox="0 0 11 16" aria-hidden="true"><path d="M2 2 L8 8 L2 14" fill="none" stroke="var(--bullet-mark)" stroke-width="3.5"/></svg>Lorem ipsum dlolor sit ipsum ipsum</li>
      <li><svg width="11" height="16" viewBox="0 0 11 16" aria-hidden="true"><path d="M2 2 L8 8 L2 14" fill="none" stroke="var(--bullet-mark)" stroke-width="3.5"/></svg>Lorem ipsum dlolor sit ipsum ipsum</li>
      <li><svg width="11" height="16" viewBox="0 0 11 16" aria-hidden="true"><path d="M2 2 L8 8 L2 14" fill="none" stroke="var(--bullet-mark)" stroke-width="3.5"/></svg>Lorem ipsum dlolor sit ipsum ipsum</li>
    </ul>
    <div class="teamwork-art" role="img" aria-label="Illustration: a blue winner figure with a medal beside orange figures stacking grey blocks together"></div>
  </main>

  <footer class="footer-band">
    <p class="brand-name">Brookvane</p>
  </footer>
</body>
</html>
```